Professional Reserve Fund Planners require print ad

The Accredited Lifecycle Budget Advising (ALB) designation is the only designated professional that has specific education in the preparation of reserve fund studies.
Reserve Fund Studies are mandatory for Condominiums across Canada and we want to promote our designation as a step above others performing studies and should be sought out by clients if they would like to have the best studies.
The advertising will require space for the Housing Stewardship Guild of Canada (HSGC) logo and the contact information for planners who have the accreditation.
Some points to consider: The designation has been in place since 1999. Specific training in the preparation of long term reserve fund studies with a specific focus on financial fundamentals, technical proficiency, investing reserves appropriately and legislation.
This will be a full page magazine ad for a trade publication called Strata Ledger by PrintHollow. Thanks.
Please note that the ads i have uploaded are simply ads that I feel capture the essence of what I am trying to achieve. I believe the ads I have uploaded are indicating a feeling of trust in the designation THEY are promoting. I want our designation ad to feel the same. You are out looking for someone to perform a reserve fund study. You can find the same old schmuck or you can find someone who has invested time and money seeking a better education and the designation ALB shows dedication, ethical standards and educational level that should give clients the feeling they are getting the best of the best.
For property managers and a Board of Directors, a properly prepared and timely reserve fund study will keep the Board of Directors and/or owners off their back. I always use the concept of "hiring us makes your job easier" and words or phrases like value-add partner, service provider, collaboration, reasonable, achievable.
Condominium owners looking for professional reserve fund study services.
Condominium Board of Directors
Condominium Property Managers

```html
<!DOCTYPE html>
<html lang="en">
<head>
<meta charset="utf-8">
<title>Accredited Lifecycle Budget Advisor – Print Ad</title>
<link rel="stylesheet" href="https://fonts.googleapis.com/css2?family=Arimo:wght@400;700&family=Open+Sans:wght@400;600;700&family=Teko:wght@500;600&family=Roboto+Condensed:ital,wght@0,400;0,700;1,400;1,700&display=swap">
<style>
  :root {
    --stage: #eeeeee;
    --paper: #f4f4f4;
    --red: #e3161f;
    --red-dark: #c40f17;
    --ink: #1a1a1a;
    --muted: #444;
    --note: #f8f8f8;
    --note-edge: #d2d2d2;
  }
  * { box-sizing: border-box; margin: 0; padding: 0; }
  html, body { width: 1200px; height: 900px; overflow: hidden; background: var(--stage); }
  .ad {
    position: absolute; left: 315px; top: 28px; width: 570px; height: 844px;
    background: repeating-linear-gradient(90deg, #f6f6f6 0 2px, #eeeeee 2px 4px);
    box-shadow: 0 6px 22px rgba(0,0,0,.18);
    overflow: hidden;
  }
  .top-rule { height: 5px; background: var(--red); }
  .brand { position: absolute; left: 26px; top: 26px; display: flex; align-items: center; gap: 10px; }
  .brand-mark { width: 40px; height: 40px; background: var(--red); }
  .brand-name { font-family: "Arimo", Arial, sans-serif; font-weight: 700; font-size: 14.5px; line-height: 1.3; color: var(--ink); }
  .photo {
    position: absolute; left: 0; top: 86px; width: 570px; height: 276px;
    background: linear-gradient(180deg, #f1f1f1 0%, #dfe3e8 45%, #c9a27a 88%, #b58a60 100%);
  }
  .tagline {
    position: absolute; left: 0; top: 234px; width: 248px; height: 70px;
    background: rgba(227,22,31,.82); color: #fff;
    font-family: "Open Sans", Arial, sans-serif; padding: 8px 0 0 18px;
  }
  .tagline .small { font-size: 16px; font-weight: 600; letter-spacing: .3px; }
  .tagline .big { font-size: 24px; font-weight: 600; line-height: 1.1; }
  .headline {
    position: absolute; left: 0; top: 364px; width: 570px; height: 52px;
    background: var(--red); color: #fff; text-align: center;
    font-family: "Teko", "Arial Narrow", sans-serif; font-weight: 600;
    font-size: 33px; letter-spacing: 1.2px; line-height: 56px;
  }
  .intro {
    position: absolute; left: 0; top: 426px; width: 570px; text-align: center;
    font-family: "Open Sans", Arial, sans-serif; font-weight: 600; font-size: 16px; line-height: 1.4; color: var(--ink);
  }
  .pillars { position: absolute; left: 24px; top: 480px; display: flex; gap: 9px; }
  .pillar {
    position: relative; width: 96px; height: 82px; background: var(--note);
    border: 1px solid var(--note-edge); box-shadow: 0 3px 4px rgba(0,0,0,.18);
    display: flex; align-items: center; justify-content: center; text-align: center;
    font-family: "Open Sans", Arial, sans-serif; font-weight: 600; font-size: 10.5px; line-height: 1.6; color: var(--ink);
  }
  .pillar:nth-child(2) { margin-top: 2px; }
  .pillar:nth-child(4) { margin-top: 4px; }
  .pillar:nth-child(5) { margin-top: 6px; }
  .pillar .clip { position: absolute; left: 6px; top: -8px; width: 9px; height: 20px; }
  .firms-bar {
    position: absolute; left: 0; top: 580px; width: 570px; height: 28px; background: var(--red);
    color: #fff; text-align: center; font-family: "Open Sans", Arial, sans-serif; font-weight: 600; font-size: 14.5px; line-height: 28px;
  }
  .firms {
    position: absolute; left: 10px; top: 618px; width: 550px;
    display: grid; grid-template-columns: repeat(3, 1fr); column-gap: 8px;
    font-family: "Roboto Condensed", "Arial Narrow", sans-serif; font-style: italic; color: var(--ink);
  }
  .firm-col { display: flex; flex-direction: column; gap: 12px; text-align: center; }
  .firm-name { font-size: 9.5px; font-weight: 700; }
  .firm-name .city { font-weight: 400; }
  .firm-contact { font-size: 9px; color: var(--muted); }
  .url-bar {
    position: absolute; left: 0; top: 790px; width: 570px; height: 30px; background: var(--red);
    color: #fff; text-align: center; font-family: "Open Sans", Arial, sans-serif; font-weight: 700; font-size: 18px; line-height: 30px; letter-spacing: .3px;
  }
</style>
</head>
<body>
<main class="ad">
  <div class="top-rule"></div>

  <header class="brand">
    <span class="brand-mark"></span>
    <div class="brand-name">Housing Stewardship Guild of Canada<br>Guilde canadienne de l'intendance</div>
  </header>

  <div class="photo" role="img" aria-label="Photograph of an advisor in a suit reviewing a laptop with a smiling senior couple at a wooden table"></div>

  <div class="tagline">
    <div class="small">SHARING KNOWLEDGE</div>
    <div class="big">SINCE 1999</div>
  </div>

  <h1 class="headline">THE ACCREDITED LIFECYCLE BUDGET ADVISOR</h1>

  <p class="intro">Seek out professionals with specific education and training in<br>Reserve Fund Study preparation</p>

  <section class="pillars">
    <div class="pillar"><svg class="clip" viewBox="0 0 9 20"><path d="M4.5 19V4a2.5 2.5 0 0 1 5 0v11" fill="none" stroke="#888" stroke-width="1.3"/><path d="M1 4a3.5 3.5 0 0 1 7 0" fill="none" stroke="#888" stroke-width="1.3"/></svg>SOUND<br>FINANCIAL<br>FUNDAMENTALS</div>
    <div class="pillar"><svg class="clip" viewBox="0 0 9 20"><path d="M4.5 19V4a2.5 2.5 0 0 1 5 0v11" fill="none" stroke="#888" stroke-width="1.3"/><path d="M1 4a3.5 3.5 0 0 1 7 0" fill="none" stroke="#888" stroke-width="1.3"/></svg>TECHNICAL<br>PROFICIENCY</div>
    <div class="pillar"><svg class="clip" viewBox="0 0 9 20"><path d="M4.5 19V4a2.5 2.5 0 0 1 5 0v11" fill="none" stroke="#888" stroke-width="1.3"/><path d="M1 4a3.5 3.5 0 0 1 7 0" fill="none" stroke="#888" stroke-width="1.3"/></svg>RESERVE<br>FUND<br>OPTIMIZATION</div>
    <div class="pillar"><svg class="clip" viewBox="0 0 9 20"><path d="M4.5 19V4a2.5 2.5 0 0 1 5 0v11" fill="none" stroke="#888" stroke-width="1.3"/><path d="M1 4a3.5 3.5 0 0 1 7 0" fill="none" stroke="#888" stroke-width="1.3"/></svg>EXCEEDING<br>LEGISLATIVE<br>REQUIREMENTS</div>
    <div class="pillar"><svg class="clip" viewBox="0 0 9 20"><path d="M4.5 19V4a2.5 2.5 0 0 1 5 0v11" fill="none" stroke="#888" stroke-width="1.3"/><path d="M1 4a3.5 3.5 0 0 1 7 0" fill="none" stroke="#888" stroke-width="1.3"/></svg>FUND<br>MANAGEMENT</div>
  </section>

  <div class="firms-bar">Look for ALB accredited professionals at the following firms</div>

  <section class="firms">
    <div class="firm-col">
      <div><div class="firm-name">Northgate Risk Partners <span class="city">| Vancouver</span></div><div class="firm-contact">www.northgaterisk.ca | 604.555.0160</div></div>
      <div><div class="firm-name">Larchmont Appraisals <span class="city">| Kelowna</span></div><div class="firm-contact">www.larchmontappraise.com | 250.555.0142</div></div>
      <div><div class="firm-name">Keystone Building Advisors <span class="city">| Coquitlam</span></div><div class="firm-contact">www.keystoneba.com | 604.555.0137</div></div>
      <div><div class="firm-name">Alder &amp; Finch Appraisals <span class="city">| New Westminster</span></div><div class="firm-contact">www.alderfinch.com | 604.555.0119</div></div>
    </div>
    <div class="firm-col">
      <div><div class="firm-name">TBR Engineering <span class="city">| Burnaby</span></div><div class="firm-contact">www.tbrengineering.com | 604.555.0171</div></div>
      <div><div class="firm-name">Halden &amp; Marsh <span class="city">| Richmond</span></div><div class="firm-contact">www.haldenmarsh.com | 604.555.0188</div></div>
      <div><div class="firm-name">Orca Reserve Consulting <span class="city">| Burnaby</span></div><div class="firm-contact">www.orcareserve.ca | 604.555.0128</div></div>
      <div><div class="firm-name">Whitlow, Barnes &amp; Co <span class="city">| Vancouver</span></div><div class="firm-contact">www.whitlowbarnes.com | 604.555.0143</div></div>
    </div>
    <div class="firm-col">
      <div><div class="firm-name">Pemberly &amp; Associates <span class="city">| Vancouver</span></div><div class="firm-contact">www.pemberlyplanning.com | 604.555.0161</div></div>
      <div><div class="firm-name">Upkeep Planning Group <span class="city">| Cloverdale</span></div><div class="firm-contact">www.upkeepgroup.ca | 604.555.0135</div></div>
      <div><div class="firm-name">Ridley &amp; Vance Appraisals <span class="city">| Campbell River</span></div><div class="firm-contact">www.ridleyvance.net | 250.555.0195</div></div>
      <div><div class="firm-name">Clearview Estate Advisors <span class="city">| Trail</span></div><div class="firm-contact">www.clearviewestate.com | 1.877.555.0124</div></div>
    </div>
  </section>

  <div class="url-bar">www.hsgc.ca/en/designations-alb</div>
</main>
</body>
</html>
```